Corporate Design für Immobilienfirma
Zielgruppe
Immobilienmakler für Wohn- und Gewerbeimmobilien, Immobilienbewertung, Immobilienberatung, freiberufliche Dozentin
Aufgabenstellung
Das Design sollte hochwertig und seriös wirken, nicht verspielt, stattdessen gradlinig. Bitte jedoch nicht zu exklusiv, da sich der Standort der Firma in einem Gebiet mit weniger Potenzial (keine Ballungsgebiete wie Düsseldort, Hamburg, Köln oder Berlin) befindet. Es muss daher die breite Zielgruppe angesprochen werden, jedoch meine Immobilienkompetenz ausstrahlen. Bitte keine verspielten Häuser oder Dächer im Logo
Das MB sollte möglichst ineinander verschlungen sein, sprich das J und das K sich den "Strich" in der Mitte teilen. Dieser Strich sollte sich dann möglichst nach unten verlängern, sodass hieraus gleichzeitig das "Immobilien" hervorgeht.
Ich bin jung, dynamisch und möchte anders als die Makler hier in der Umgebung arbeiten, bin zudem gelernte Immobilienkauffrau mit angeschlossenen Studium. Diesen Ehrgeiz sollte das Logo möglichst zum Ausdruck bringen.
Mein vollständiger Name lautet Mariella Brunst.
Bei den Farben bin ich nicht festgelegt. Entweder rein dunkleres blau mit grau oder schwarz. Bitte kein orange, grün oder zu bunt.
Was ich zudem gut fände, wenn einzelne Designer versuchen die Silhouette des Velin Museums aus Herford einzubinden, ist jedoch nicht zwingend erforderlich, jedoch würde ich gerne mal so einen Vorschlag prüfen :)
Bei Fragen oder Anregungen stehe ich gerne zur Verfügung.

```html
<!DOCTYPE html>
<html lang="de">
<head>
<meta charset="utf-8">
<title>MB Immobilien – Geschäftsausstattung</title>
<link rel="stylesheet" href="https://fonts.googleapis.com/css2?family=Arimo:wght@400;700&display=swap">
<style>
  :root{
    --bg:#e6e6e6;
    --paper:#ffffff;
    --ink:#111111;
    --text:#333333;
    --muted:#666666;
    --shadow:0 4px 14px rgba(0,0,0,.18);
  }
  *{box-sizing:border-box;margin:0;padding:0}
  html,body{width:1200px;height:1200px;overflow:hidden}
  body{background:var(--bg);font-family:"Arimo",Arial,sans-serif;color:var(--text);position:relative}

  .brand{display:flex;align-items:center;gap:10px;font-family:"Arimo",Arial,sans-serif;font-weight:700;color:var(--ink);letter-spacing:.04em;white-space:nowrap;text-transform:uppercase}
  .brand-square{background:currentColor;flex:none}

  /* Letterhead */
  .letterhead{position:absolute;left:60px;top:60px;width:580px;height:820px;background:var(--paper);box-shadow:var(--shadow);padding:44px 56px;font-size:9.5px;line-height:1.45}
  .letterhead .brand{justify-content:center;font-size:17px}
  .letterhead .brand-square{width:14px;height:14px}
  .lh-mark{position:absolute;right:44px;top:70px;width:14px;height:40px;background:var(--ink)}
  .sender{margin-top:22px;font-size:7.5px;color:var(--muted);border-bottom:1px solid #bbb;display:inline-block;padding-bottom:1px}
  .recipient{margin-top:4px;font-size:8.5px}
  .salutation{margin-top:70px}
  .letter-body p{margin-top:10px;text-align:justify}
  .closing{margin-top:22px}
  .signature{margin-top:22px}
  .lh-footer{position:absolute;left:56px;right:56px;bottom:44px;display:flex;justify-content:space-between;align-items:flex-start;font-size:8px;line-height:1.4}
  .foot-col{border-left:5px solid var(--ink);padding-left:8px;min-height:56px}
  .foot-col:nth-child(2){margin-top:14px}
  .foot-col:nth-child(3){margin-top:28px}

  /* Cards */
  .card{position:absolute;background:var(--paper);box-shadow:var(--shadow);overflow:hidden}
  .card-lg{width:400px;height:250px}
  .card-sm{width:340px;height:212px}
  .card-front-dark{left:740px;top:60px;background:var(--ink);display:flex;align-items:center;justify-content:center}
  .card-front-dark .brand{color:#fff;font-size:26px}
  .card-front-dark .brand-square{width:20px;height:20px}

  .card-back{left:740px;top:340px;padding:28px 30px;font-size:11px}
  .card-back .brand{font-size:19px}
  .card-back .addr{margin-top:12px;line-height:1.45}
  .card-back .mark{position:absolute;right:36px;top:26px;width:16px;height:40px;background:var(--ink)}
  .card-back .contact{position:absolute;left:30px;right:30px;bottom:30px;display:flex;justify-content:space-between;align-items:flex-end;font-size:9.5px;line-height:1.5}
  .card-back .base{position:absolute;left:0;right:0;bottom:0;height:8px;background:var(--ink)}

  .card-logo{left:740px;top:620px;display:flex;align-items:center;justify-content:center}
  .card-logo .brand{font-size:24px}
  .card-logo .brand-square{width:18px;height:18px}

  /* Card variants */
  .variant{top:930px;font-size:9.5px;line-height:1.5}
  .variant-a{left:60px;padding:24px 26px}
  .variant-a .brand{font-size:14px}
  .variant-a .info{margin-top:22px}
  .variant-a .corner{position:absolute;right:0;bottom:0;width:110px;height:38px;background:var(--ink);display:flex;align-items:center;justify-content:center}
  .variant-a .corner .brand{color:#fff;font-size:12px}
  .variant-a .corner .brand-square{width:9px;height:9px}

  .variant-b{left:430px}
  .variant-b .band{position:absolute;left:0;right:0;top:40px;height:62px;background:var(--ink);display:flex;align-items:center;justify-content:center}
  .variant-b .band .brand{color:#fff;font-size:16px}
  .variant-b .band .brand-square{width:12px;height:12px}
  .variant-b .line{position:absolute;left:0;right:0;top:108px;height:3px;background:var(--ink)}
  .variant-b .cols{position:absolute;left:24px;right:24px;bottom:22px;display:flex;justify-content:space-between}

  .variant-c{left:800px}
  .variant-c .brand{position:absolute;left:0;right:0;top:42px;justify-content:center;font-size:17px}
  .variant-c .brand-square{width:13px;height:13px}
  .variant-c .cols{position:absolute;left:24px;right:24px;bottom:24px;display:flex;justify-content:space-between}
  .variant-c .rule{position:absolute;left:24px;right:24px;bottom:78px;height:1px;background:var(--ink)}
  b{font-weight:700;color:var(--ink)}
</style>
</head>
<body>

<article class="letterhead">
  <div class="brand"><span class="brand-square"></span>MB Immobilien</div>
  <span class="lh-mark"></span>
  <div class="sender">Name · Adresse 1 · Adresse 2</div>
  <div class="recipient">Max Mustermann<br>Straße<br>Ort</div>

  <p class="salutation">Sehr geehrter Herr,</p>
  <div class="letter-body">
    <p>Vielen Dank für Ihr Interesse an unserem Angebot. Gerne senden wir Ihnen anbei die gewünschten Unterlagen zu Ihrer Immobilie.</p>
    <p>Nach unserer Besichtigung haben wir den Wert Ihres Hauses sorgfältig ermittelt. Die Bewertung berücksichtigt Lage, Zustand, Ausstattung und die aktuelle Marktlage in der Region. Auf dieser Grundlage empfehlen wir einen realistischen Angebotspreis, der schnelle und faire Verhandlungen ermöglicht.</p>
    <p>Auf Wunsch erstellen wir ein ausführliches Exposé mit Grundrissen und Beschreibung. Für Rückfragen stehen wir Ihnen jederzeit gern zur Verfügung.</p>
    <p>Wir freuen uns auf eine angenehme Zusammenarbeit und melden uns in den nächsten Tagen telefonisch bei Ihnen.</p>
  </div>
  <p class="closing">Mit freundlichen Grüßen</p>
  <p class="signature">Name<br>Geschäftsführer</p>

  <footer class="lh-footer">
    <div class="foot-col">Name<br>Adresse 1<br>Adresse 2</div>
    <div class="foot-col">Tel.: +49 (0) 123456<br>Fax: +49 (0) 123456<br>E-Mail: info@brunst-beispielhaus.de</div>
    <div class="foot-col">Bankverbindung: xxxxxxxxx<br>IBAN: xxxxxxxxxxxxxxx<br>BIC: xxxxxxxxxxxxxxx</div>
  </footer>
</article>

<section class="card card-lg card-front-dark">
  <div class="brand"><span class="brand-square"></span>MB</div>
</section>

<section class="card card-lg card-back">
  <div class="brand">MB Immobilien</div>
  <span class="mark"></span>
  <div class="addr">Adresse 1<br>Adresse 2</div>
  <div class="contact">
    <div>Mob.: 01234 000000<br>Tel.: 01234 000000<br>Fax: 01234 000000</div>
    <div>E-Mail: info@brunst-beispielhaus.de<br>Web: brunst-beispielhaus.de</div>
  </div>
  <span class="base"></span>
</section>

<section class="card card-lg card-logo">
  <div class="brand"><span class="brand-square"></span>MB Immobilien</div>
</section>

<section class="card card-sm variant variant-a">
  <div class="brand">MB Immobilien</div>
  <div class="info">Adresse<br>Adresse<br><br><b>Tel:</b> +49 1 12345<br><b>Fax:</b> +49 1 123456<br><b>Email:</b> office@brunst-beispielhaus.de</div>
  <div class="corner"><div class="brand"><span class="brand-square"></span>MB</div></div>
</section>

<section class="card card-sm variant variant-b">
  <div class="band"><div class="brand"><span class="brand-square"></span>MB Immobilien</div></div>
  <span class="line"></span>
  <div class="cols">
    <div>Adresse 1<br>Adresse 2</div>
    <div>T: 01234 000000<br>F: 01234 000000<br>brunst-beispielhaus.de</div>
  </div>
</section>

<section class="card card-sm variant variant-c">
  <div class="brand"><span class="brand-square"></span>MB Immobilien</div>
  <span class="rule"></span>
  <div class="cols">
    <div>Adresse 1<br>Adresse 2</div>
    <div><b>tel.</b> 01234 000000<br><b>mobile</b> 01234 000000<br><b>email</b> info@brunst-beispielhaus.de</div>
  </div>
</section>

</body>
</html>
```